Tolland IT Services needs to look professional and modern

This is my first time using this site so I am unsure what to expect, I am very serious in needing design work done and have no issues paying for it. I am hoping for good things as my business needs this before I can make any money !
Tolland IT Services Pty Ltd core business is small / medium business networking, support and related hardware ie servers, PC's, Laptops, network equipment/infrastructure, printers etc
The focus of the business to give our customers a competitive edge over others by using new and innovative technologies and services. This is always balanced against stability, reliability and efficiency of the customers IT network.
We are looking for the design of a logo and business cards (there is also the potential for a website once this project is successfully completed). The design should have a sense of refinement and stability while being modern. The choice of colour pallet is up to the designer but nothing gordy.
The cards need to be double sided with the reverse to include brief points of business offered, details of points to be filled in by me later.
The front needs to include business name, mobile number (0472 593 168), my name (Dean Tolland), email address (dean@TollandITServices.example.com.au), website address (www.TollandITServices.example.com.au), business slogan ("Your Competitive Edge")
"Your Competitive Edge"

```html
<!DOCTYPE html>
<html lang="en">
<head>
<meta charset="utf-8">
<title>Tolland IT Services – Logo and Business Cards</title>
<link rel="stylesheet" href="https://fonts.googleapis.com/css2?family=Open+Sans:ital,wght@0,700;1,700&display=swap">
<style>
  :root {
    --page: #ffffff;
    --ink: #3d3d3f;
    --blue-light: #3aa6e6;
    --blue-mid: #1a7fc9;
    --blue-deep: #0d5ea8;
    --silver-light: #eeeeee;
    --silver-dark: #8f9296;
    --card: #ffffff;
    --white: #ffffff;
  }
  * { margin: 0; padding: 0; box-sizing: border-box; }
  html, body {
    width: 1200px; height: 551px; overflow: hidden;
    background: var(--page);
    font-family: "Open Sans", Arial, sans-serif;
  }
  .canvas { position: relative; width: 1200px; height: 551px; }

  .brand-lockup {
    position: absolute; left: 262px; top: 128px; width: 196px;
    display: flex; flex-direction: column; align-items: center;
  }
  .brand-lockup__mark {
    width: 150px; height: 150px; border-radius: 50%;
    background: radial-gradient(circle at 38% 35%, var(--silver-light), #c9cbce 70%, var(--silver-dark));
  }
  .brand-lockup__name {
    margin-top: 26px; font-size: 23px; font-weight: 700;
    color: var(--ink); white-space: nowrap;
  }

  .card {
    position: absolute; left: 741px; width: 378px; height: 231px;
    background: var(--card); overflow: hidden;
    box-shadow: 0 2px 8px rgba(0,0,0,.35);
  }
  .card--front { top: 34px; }
  .card--back { top: 290px; }
  .card__wave { position: absolute; inset: 0; width: 100%; height: 100%; }

  .card__details {
    position: absolute; left: 13px; top: 8px; color: var(--white);
    font-style: italic; font-weight: 700; line-height: 1.28;
  }
  .card__company { font-size: 26px; line-height: 1.25; margin-bottom: 3px; }
  .card__line { font-size: 16px; }
  .card__line--phone { padding-left: 3px; font-size: 17px; }

  .card__emblem {
    position: absolute; left: 247px; top: 106px; width: 88px; height: 88px;
    border-radius: 50%;
    background: radial-gradient(circle at 38% 35%, var(--silver-light), #c9cbce 70%, var(--silver-dark));
  }
  .card__slogan {
    position: absolute; right: 22px; bottom: 6px;
    font-size: 15.5px; font-style: italic; font-weight: 700; color: var(--ink);
  }

  .card__faint-circle {
    position: absolute; left: 180px; top: 8px; width: 222px; height: 222px;
    border-radius: 50%; background: #f3f4f5;
  }
  .card__statement {
    position: absolute; left: 71px; top: 73px; width: 280px;
    font-size: 12.3px; font-style: italic; font-weight: 700;
    color: var(--ink); line-height: 1.3;
  }
</style>
</head>
<body>
<main class="canvas">

  <section class="brand-lockup" aria-label="Logo">
    <div class="brand-lockup__mark"></div>
    <p class="brand-lockup__name">Tolland IT Services</p>
  </section>

  <section class="card card--front" aria-label="Business card front">
    <svg class="card__wave" viewBox="0 0 378 231" preserveAspectRatio="none" aria-hidden="true">
      <defs>
        <linearGradient id="blueField" x1="0" y1="0" x2="1" y2="1">
          <stop offset="0" stop-color="var(--blue-deep)"/>
          <stop offset=".5" stop-color="var(--blue-light)"/>
          <stop offset="1" stop-color="var(--blue-mid)"/>
        </linearGradient>
        <linearGradient id="silverBand" x1="0" y1="0" x2="1" y2="0">
          <stop offset="0" stop-color="var(--silver-dark)"/>
          <stop offset=".5" stop-color="var(--silver-light)"/>
          <stop offset="1" stop-color="var(--silver-dark)"/>
        </linearGradient>
      </defs>
      <path d="M0 0 H378 V72 C300 84 210 130 130 180 C80 210 30 228 0 231 Z" fill="url(#silverBand)"/>
      <path d="M0 0 H378 V58 C300 70 205 116 122 170 C78 200 30 220 0 224 Z" fill="url(#blueField)"/>
    </svg>
    <div class="card__details">
      <p class="card__company">Tolland IT Services</p>
      <p class="card__line card__line--phone">0472 593 168</p>
      <p class="card__line">dean@TollandITServices.example.com.au</p>
      <p class="card__line">TollandITServices.example.com.au</p>
    </div>
    <div class="card__emblem"></div>
    <p class="card__slogan">Your Competitive Edge</p>
  </section>

  <section class="card card--back" aria-label="Business card back">
    <div class="card__faint-circle"></div>
    <p class="card__statement">“The focus of the business to give our<br>&nbsp;customers a competitive edge<br>&nbsp;over others by using new and innovative<br>technologies and services”</p>
  </section>

</main>
</body>
</html>
```